Business Cards for Marco and Tobin

Design of business cards for two people with the recently created brand Valcor Mobile. Valcor Mobile wants to become a worldwide major player on the secondhand phone market. It gathers send hand phones from individuals, refurbish them and sell them throughout the world. It has a green impact (recycling) and we also contribute to social project in Africa (a percentage of our benefits are sent to build school, sport facilities, etc.

Target Market(s)

B2B - Marco and Tobin are in contact with distributors across Africa.

Industry/Entity Type

Wireless Communication

Contact Information for Business Card

Marco Feuillet
Head of Emerging Markets
Valcor Energy South Africa (Pty) Ltd
Kestrel Road 47
2031 Sandton - Johannesburg
South Africa
Tel: + 27 10 555 0148
Mobile : +27 82 55 104
Email : marco.feuillet@valcormobile.example
Skype: marco.feuillet
Web: www.valcormobile.example
 

Tobin Farrow
Head of Southern Africa
Kestrel Road 47
South Africa
Tel: + 27 10 555 0148
Mobile: +27 83 555 0276
Email: tobin.farrow@valcormobile.example
Skype: tobin.farrow
Web: www.valcormobile.example

Requirements
Must have
• The cards need to be "serious", trustable, with a worldwide presence.
Nice to have
• Some "green" / recycling touch would be nice but not necessary if in contradiction with the general design.

```html
<!DOCTYPE html>
<html lang="en">
<head>
<meta charset="utf-8">
<title>Valcor Mobile – Business Card</title>
<link rel="stylesheet" href="https://fonts.googleapis.com/css2?family=Bebas+Neue&family=Montserrat:wght@600;700&family=Work+Sans:wght@300;400&display=swap">
<style>
  :root {
    --backdrop: #2a2a2c;
    --navy: #0d2b47;
    --paper: #ffffff;
    --accent: #1e8fd6;
    --ink: #1c2f45;
    --ink-soft: #34465a;
  }
  * { box-sizing: border-box; margin: 0; padding: 0; }
  html, body { width: 1200px; height: 900px; overflow: hidden; }
  body {
    background: var(--backdrop);
    display: flex;
    flex-direction: column;
    align-items: center;
    justify-content: center;
    gap: 36px;
    font-family: "Work Sans", sans-serif;
  }
  .card {
    width: 700px;
    height: 400px;
    position: relative;
    box-shadow: 0 10px 30px rgba(0,0,0,.45);
  }
  .card--front {
    background: var(--navy);
    display: flex;
    align-items: center;
    justify-content: center;
  }
  .brand-name {
    font-family: "Montserrat", sans-serif;
    font-weight: 700;
    font-size: 44px;
    color: var(--paper);
    letter-spacing: -0.5px;
  }
  .card--back { background: var(--paper); color: var(--ink); }
  .company {
    position: absolute;
    top: 50px;
    left: 0; right: 0;
    text-align: center;
    font-family: "Montserrat", sans-serif;
    font-weight: 600;
    font-size: 23px;
    color: var(--navy);
  }
  .identity {
    position: absolute;
    top: 160px;
    left: 70px;
    width: 240px;
  }
  .person-name {
    font-family: "Bebas Neue", sans-serif;
    font-size: 40px;
    line-height: 1;
    color: var(--accent);
    letter-spacing: 0.5px;
  }
  .person-role {
    font-weight: 300;
    font-size: 17px;
    color: var(--ink-soft);
    margin-top: 2px;
  }
  .divider {
    position: absolute;
    left: 330px;
    top: 150px;
    width: 1.5px;
    height: 100px;
    background: var(--accent);
  }
  .contacts {
    position: absolute;
    left: 355px;
    top: 150px;
    list-style: none;
    font-weight: 400;
    font-size: 17px;
    line-height: 22px;
    color: var(--ink);
  }
  .contacts li { display: flex; align-items: center; gap: 10px; white-space: nowrap; }
  .contacts svg { width: 12px; height: 12px; flex: none; }
  .contacts .hl { color: var(--accent); }
  .address {
    position: absolute;
    bottom: 48px;
    left: 0; right: 0;
    text-align: center;
    font-weight: 400;
    font-size: 18px;
    color: var(--ink-soft);
  }
</style>
</head>
<body>
  <section class="card card--front">
    <span class="brand-name">Valcor Mobile</span>
  </section>

  <section class="card card--back">
    <h1 class="company">Valcor Energy South Africa (Pty) Ltd</h1>

    <div class="identity">
      <div class="person-name">MARCO FEUILLET</div>
      <div class="person-role">Head of Emerging Markets</div>
    </div>

    <div class="divider"></div>

    <ul class="contacts">
      <li>
        <svg viewBox="0 0 12 12" aria-hidden="true"><path d="M3 1 L4.5 3.5 L3.5 4.6 Q4.8 7.2 7.4 8.5 L8.5 7.5 L11 9 L10 11 Q4 10.5 1 2 Z" fill="var(--accent)"/></svg>
        + 27 10 555 0148
      </li>
      <li>
        <svg viewBox="0 0 12 12" aria-hidden="true"><rect x="3" y="1" width="6" height="10" rx="1" fill="none" stroke="var(--accent)" stroke-width="1.3"/><circle cx="6" cy="9.2" r=".7" fill="var(--accent)"/></svg>
        +27 82 55 104
      </li>
      <li>
        <svg viewBox="0 0 12 12" aria-hidden="true"><circle cx="6" cy="6" r="5" fill="var(--accent)"/></svg>
        marco.feuillet
      </li>
      <li>
        <svg viewBox="0 0 12 12" aria-hidden="true"><g fill="none" stroke="var(--accent)" stroke-width="1"><circle cx="6" cy="6" r="5"/><ellipse cx="6" cy="6" rx="2.2" ry="5"/><line x1="1" y1="6" x2="11" y2="6"/></g></svg>
        <span>www.<span class="hl">valcormobile</span>.example</span>
      </li>
      <li>
        <svg viewBox="0 0 12 12" aria-hidden="true"><g fill="none" stroke="var(--accent)" stroke-width="1.2"><rect x="1" y="2.5" width="10" height="7"/><polyline points="1,2.5 6,6.5 11,2.5"/></g></svg>
        marco.feuillet@valcormobile.example
      </li>
    </ul>

    <p class="address">Kestrel Road 47, 2031 Sandton - Johannesburg South Africa</p>
  </section>
</body>
</html>
```